Franchise Beratung sucht Flyer Design
Mara hat das Faltblatt sehr professionell gestaltet! Was mir besonders gefällt ist die Tatsache, dass sie sich in das ausgefallene Thema Franchise sehr gut eingedacht hat, was bei der Auswahl der Bilder gut zu sehen ist. Außerdem hat sie den Text noch ergänzt und verbessert.
Zielgruppe
CapstoneGrowers ist eine Unternehmensberatung, die sich auf den Aufbau von neuen Franchisesystemen spezialisiert hat. Dabei setzen wir von Anfang an auf die Digitalisierung des Systems, um es leistungsstark und schnell zu gestalten.
Zielgruppe:
Der Flyer richtet sich vor allem an Unternehmer, die über die Expansion durch Franchising nachdenken. Er soll zur Kontaktaufnahme anregen und die klassischen Vorbehalte (zu teuer, brauche ich nicht, kann ich mir nicht leisten) nehmen.
Aufgabenstellung
Bei Form und Gestalt sind wir offen - er sollte aber sinnvoll auch per Post versendet werden können. Das Design sollte sich an unsere Website anpassen. Klar, modern und eher puristisch. Es darf aber ruhig etwas mehr Farbe verwendet werden.
Zusätzlich zu der Print-Vorlage möchten wir auch eine Version, die wir sinnvoll per Mail verschicken können.
Der Gewinner-Flyer sollte beschreibbar sein, so dass wir zukünftig einzelne Textpassagen ändern können.
Falls es Verbesserungsvorschläge zum Text gibt, sind auch diese herzlich willkommen!
Farben:
CMYK: 49 / 38 / 43 / 3 ( dunkelgrau )
CMYK: 24 / 17 / 21 / 0 ( hellgrau )
CMYK: 54 / 200 / 100/ 2 ( grün )
Schrifttyp: Für das Logo wurde eine eigene Schrift genutzt, da fehlen aber leider manche Buchstaben, deshalb möchten wir lieber eine andere Schrift, die gut zum Logo passt.

```html
<!DOCTYPE html>
<html lang="de">
<head>
<meta charset="utf-8">
<title>CapstoneGrowers – Faltblatt</title>
<link rel="stylesheet" href="https://fonts.googleapis.com/css2?family=Open+Sans:ital,wght@0,400;0,600;0,700;0,800;1,400&display=swap">
<style>
  :root{
    --stage:#c3c6d0;
    --divider:#ffffff;
    --paper:#fbfbfb;
    --paper-shade:#ececec;
    --frame:#c9c9c9;
    --sky:#a9c0cc;
    --sky-deep:#98b1bf;
    --green:#7ab51d;
    --green-light:#93c01f;
    --text:#2b2b2b;
    --muted:#8b8b8b;
    --photo:#e4e4e2;
  }
  *{box-sizing:border-box;margin:0;padding:0}
  html,body{width:1200px;height:2585px;overflow:hidden}
  body{background:var(--stage);font-family:"Open Sans",Arial,sans-serif;color:var(--text);position:relative}
  .scene{position:absolute;left:0;width:1200px;background:var(--stage)}
  .scene--cover{top:0;height:862px}
  .scene--inside{top:872px;height:862px}
  .scene--outside{top:1744px;height:841px}
  .divider{position:absolute;left:0;width:1200px;height:10px;background:var(--divider)}

  .panel{position:absolute;background:var(--paper);box-shadow:0 18px 40px rgba(60,64,80,.25);overflow:hidden}
  .panel__frame{position:absolute;inset:14px;border:1px solid var(--frame);pointer-events:none}

  /* Cover */
  .cover{width:360px;height:680px}
  .cover__art{position:absolute;left:14px;top:14px;right:14px;height:420px}
  .cover__brand{position:absolute;left:0;right:0;top:460px;text-align:center}
  .brand{display:inline-flex;align-items:center;gap:10px}
  .brand__dot{width:18px;height:18px;border-radius:50%;background:var(--green)}
  .brand__name{font-size:28px;font-weight:400;color:var(--green);letter-spacing:-.5px}
  .brand__claim{display:block;font-size:9px;letter-spacing:4px;color:var(--muted);margin-top:2px}
  .cover__code{position:absolute;right:26px;top:410px;font-size:9px;font-weight:700;color:#333}
  .cover__headline{position:absolute;left:0;right:0;top:560px;text-align:center;color:var(--green);font-weight:800;font-size:18px;line-height:1.25;text-transform:uppercase;letter-spacing:.5px}

  /* Inside spread */
  .spread{width:940px;height:640px}
  .spread__left,.spread__right{position:absolute;top:0;bottom:0;width:470px}
  .spread__left{left:0;background:var(--paper)}
  .spread__right{right:0;background:linear-gradient(90deg,var(--paper-shade),var(--paper) 40%)}
  .spread__left .panel__frame{right:0;border-right:none}
  .spread__right .panel__frame{left:0;border-left:none}
  .copy{position:absolute;left:56px;right:34px;top:36px;font-size:12.5px;line-height:1.5}
  .spread__right .copy{left:36px;right:46px;top:118px}
  .copy .brand__name{font-size:26px}
  .copy h2{color:var(--green);font-weight:800;font-size:16px;line-height:1.2;margin:26px 0 12px}
  .copy h2.wide{font-size:17px}
  .copy p{margin-bottom:12px}
  .copy .justify{text-align:justify}
  .offer{display:flex;gap:14px;align-items:flex-start;margin-top:12px}
  .offer__icon{flex:0 0 44px;height:44px;border-radius:50%;background:linear-gradient(#dfe8cc,#b9d38a);margin-top:6px}
  .offer p{margin:0;font-size:12.2px}

  /* Outside spread */
  .outside{width:760px;height:640px}
  .back,.front{position:absolute;top:0;bottom:0;width:380px}
  .back{left:0}
  .front{right:0;border-left:1px solid #e3e3e3}
  .back .panel__frame{border-color:var(--green)}
  .back__photo{position:absolute;left:14px;top:14px;right:14px;height:360px;background:linear-gradient(160deg,#f4f4f2,var(--photo) 60%,#cfcfcc)}
  .back__band{position:absolute;left:14px;right:14px;bottom:14px;height:270px}
  .back__text{position:absolute;left:40px;right:30px;bottom:44px;color:#fff;font-size:12.5px;line-height:1.5}
  .back__text strong{font-size:13px;display:block;margin-bottom:12px}
  .back__text p{margin-bottom:12px}
  .contact{display:flex;align-items:center;gap:8px}
  .front .cover__art{height:390px}
  .front .cover__code{top:380px}
  .front .cover__brand{top:430px}
  .front .cover__headline{top:530px}
</style>
</head>
<body>

<section class="scene scene--cover">
  <article class="panel cover" style="left:420px;top:90px">
    <svg class="cover__art" viewBox="0 0 332 420" preserveAspectRatio="none" role="img" aria-label="Illustration: Geschäftsmann im Comicstil hält einen Laden mit grüner Markise, umgeben von kleinen Filialen in Blasen">
      <path d="M0 0H332V395Q166 440 0 395Z" fill="var(--sky)"/>
    </svg>
    <span class="cover__code">#1099</span>
    <div class="cover__brand">
      <span class="brand"><span class="brand__dot"></span><span class="brand__name">CapstoneGrowers</span></span>
      <span class="brand__claim">Beratung Franchise-Systeme</span>
    </div>
    <p class="cover__headline">Franchising – wir lassen<br>Ihre Werte wachsen!</p>
    <div class="panel__frame"></div>
  </article>
</section>
<div class="divider" style="top:862px"></div>

<section class="scene scene--inside">
  <article class="panel spread" style="left:130px;top:110px">
    <div class="spread__left">
      <div class="panel__frame"></div>
      <div class="copy">
        <span class="brand"><span class="brand__dot"></span><span class="brand__name">CapstoneGrowers</span></span>
        <span class="brand__claim">Beratung Franchise-Systeme</span>
        <h2>CapstoneGrowers<br>Ihre Franchise-Beratung</h2>
        <p>Wer kurzfristig denkt, denkt langfristig falsch.<br>Das gilt besonders beim Aufbau eines Franchisesystems.</p>
        <p>Unternehmer, die erfolgreich ins Franchising starten wollen, setzen deshalb auf CapstoneGrowers. Durch unsere langjährige Expertise wissen wir, was wann zu tun ist. Dabei setzen wir auf digitale Medien und Tools, um das System leistungsstark und zukunftssicher zu gestalten – damit Ihre Werte wachsen!</p>
        <h2 class="wide">Wie funktioniert modernes Franchising?</h2>
        <p class="justify">Franchising ist der moderne und sympathische Weg, das eigene Unternehmen wachsen zu lassen. Das Know-how und die Marke, die Sie als Unternehmer über viele Jahre mühsam aufgebaut haben, geben Sie als Franchisegeber systematisch weiter. Und zwar an Menschen, die sich für Ihre Idee begeistern und sie mit lokalem Unternehmertum an neuen Orten zum Leben erwecken – die Franchisenehmer.</p>
        <p class="justify">Je besser Sie sich und Ihr Team dabei organisieren, desto leistungsfähiger können Sie agieren. CapstoneGrowers setzt deshalb von Anfang an auf digitale Bausteine. Dadurch bleiben die Anfangsinvestitionen für Sie überschaubar und Sie können die Franchisenehmer optimal unterstützen. <strong>Davon profitiert das gesamte System!</strong></p>
      </div>
    </div>
    <div class="spread__right">
      <div class="panel__frame"></div>
      <div class="copy">
        <h2 style="margin-top:0">Wie können wir Sie<br>auf Ihrem Weg unterstützen?</h2>
        <p>CapstoneGrowers – unser Name ist unsere Mission – wir unterstützen zukünftige Lizenz- und Franchisegeber individuell nach ihren Bedürfnissen, ihrem Budget und in ihrem Tempo.</p>
        <div class="offer"><span class="offer__icon" role="img" aria-label="Kleine Figur: der Ungeduldige"></span><p>Die <strong>Ungeduldigen</strong> mit dem <strong>Franchise Quick-Check.</strong> Sie erfahren an einem Tag, ob Ihre Idee franchisetauglich ist und was die nächsten Schritte sind.</p></div>
        <div class="offer"><span class="offer__icon" role="img" aria-label="Kleine Figur: der Entwickler"></span><p>Die <strong>Entwickler</strong> mit <strong>Franchise-Coaching.</strong> Sie entwickeln Ihr Konzept und wir steuern unser Fachwissen sowie unser Netzwerk bei.</p></div>
        <div class="offer"><span class="offer__icon" role="img" aria-label="Kleine Figur: der Wissbegierige"></span><p>Die <strong>Wissbegierigen</strong> durch <strong>interaktive Webinare.</strong> Lernen Sie alles rund um den Franchise-Aufbau bequem vom Büro aus in kleinen Einheiten. Sie entwickeln Ihr Konzept in Ihrem Tempo.</p></div>
        <div class="offer"><span class="offer__icon" role="img" aria-label="Kleine Figur: der Macher"></span><p>Die <strong>Macher</strong> durch <strong>ausgefeilte Konzepte.</strong> Wir halten Ihnen den Rücken frei und übernehmen komplett die konzeptionelle Arbeit – natürlich in enger Abstimmung mit Ihnen.</p></div>
        <div class="offer"><span class="offer__icon" role="img" aria-label="Kleine Figur: der Sparsame"></span><p>Für <strong>Sparsame</strong> per <strong>TalkLine.</strong> Statt Zeit und Geld in die Anreise zu investieren, unterstützen wir Sie gerne auch per Videokonferenz.</p></div>
      </div>
    </div>
  </article>
</section>
<div class="divider" style="top:1734px"></div>

<section class="scene scene--outside">
  <article class="panel outside" style="left:220px;top:100px">
    <div class="back">
      <div class="back__photo" role="img" aria-label="Foto: Beraterin mit langen blonden Haaren in weißer Bluse und dunkler Weste vor hellem Hintergrund"></div>
      <svg class="back__band" viewBox="0 0 352 270" preserveAspectRatio="none" aria-hidden="true">
        <path d="M0 20Q176 -10 352 40V270H0Z" fill="var(--green-light)"/>
      </svg>
      <div class="back__text">
        <strong>Neugierig geworden?</strong>
        <p>Dann sollten wir uns kennenlernen.<br>Wir freuen uns auf Ihren Anruf!</p>
        <p>
          <span class="contact"><svg width="12" height="12" viewBox="0 0 24 24" aria-hidden="true"><path fill="#fff" d="M6.6 10.8a15 15 0 0 0 6.6 6.6l2.2-2.2c.3-.3.7-.4 1-.2 1.1.4 2.3.6 3.6.6.6 0 1 .4 1 1V20c0 .6-.4 1-1 1A17 17 0 0 1 3 4c0-.6.4-1 1-1h3.5c.6 0 1 .4 1 1 0 1.3.2 2.5.6 3.6.1.3 0 .7-.2 1z"/></svg>Tel. 0211-5550142</span>
          <span class="contact"><svg width="12" height="12" viewBox="0 0 24 24" aria-hidden="true"><path fill="#fff" d="M2 5h20v14H2zm2 2v.5l8 5 8-5V7l-8 5z"/></svg>info@CapstoneGrowers.de</span>
        </p>
        <p>Mehr Informationen unter<br>www.CapstoneGrowers.de</p>
      </div>
      <div class="panel__frame"></div>
    </div>
    <div class="front">
      <svg class="cover__art" viewBox="0 0 352 390" preserveAspectRatio="none" role="img" aria-label="Illustration: Geschäftsmann im Comicstil hält einen Laden mit grüner Markise, umgeben von kleinen Filialen in Blasen">
        <path d="M0 0H352V365Q176 410 0 365Z" fill="var(--sky)"/>
      </svg>
      <span class="cover__code">#1099</span>
      <div class="cover__brand">
        <span class="brand"><span class="brand__dot"></span><span class="brand__name">CapstoneGrowers</span></span>
        <span class="brand__claim">Beratung Franchise-Systeme</span>
      </div>
      <p class="cover__headline">Franchising – wir lassen<br>Ihre Werte wachsen!</p>
      <div class="panel__frame"></div>
    </div>
  </article>
</section>

</body>
</html>
```